Geschäftspapiere für unternehmerische Holding für Beteiligungen, Projektgesellschaften und kaufmännische Steuerung
Zielgruppe
Die Hollwen GmbH ist eine unternehmerische Holding für Beteiligungen, Projektgesellschaften und kaufmännische Steuerung. Sie übernimmt Management-, Controlling- und Strukturierungsaufgaben für verbundene Unternehmen.
Zielgruppe sind Banken, Investoren, Geschäftspartner, Steuerberater, Rechtsanwälte, Behörden sowie Geschäftsführungen und Gesellschafter von Beteiligungs- und Projektgesellschaften.
Aufgabenstellung
Gesucht wird ein digitales Briefpapier für die Hollwen GmbH, das sowohl als PDF/Dokumentvorlage als auch beim Ausdruck professionell funktioniert.
Wichtig ist ein sehr klarer, hochwertiger und seriöser Auftritt. Das Design soll reduziert, strukturiert und geschäftlich wirken – keine verspielten Elemente, keine überladenen Grafiken, keine auffälligen Muster.
Das Briefpapier muss drucktauglich sein. Bitte ausreichende Druckränder und Sicherheitsabstände berücksichtigen, damit Kopf- und Fußbereich auch auf normalen Büro- und Laserdruckern sauber ausgegeben werden können. Das Layout soll sowohl digital als auch gedruckt stimmig aussehen.
Format: DIN A4 Hochformat.
Gewünschte Inhalte:
* Logo der Hollwen GmbH
* Firmenname: Hollwen GmbH
* Geschäftsanschrift: Lindauer Weg 52, 80339 München
* Telefon: 089 58210946
* E-Mail: info@hollwenbeta.example
* Webseite: hollwenbeta.example
* Geschäftsführung: Dipl.-Wirtschaftsing. (FH) Till Osterwald
* Registergericht / Amtsgericht München HRB 527081
* Bankverbindung IBAN DE918204 5571 0009 1826 40
Besonderer Wert liegt auf:
* hochwertiger Holding-/Investment-Anmutung
* sehr guter Lesbarkeit
* klarer Kopf- und Fußzeile
* sauberer Typografie
* professioneller Nutzbarkeit für Angebote, Verträge, Behörden- und Bankkorrespondenz
Bitte das Design so anlegen, dass es später als editierbare Word-/PDF-Vorlage genutzt werden kann und sowohl das Logo, als auch die Farben entsprechend verwenden.

```html
<!DOCTYPE html>
<html lang="de">
<head>
<meta charset="utf-8">
<title>Hollwen GmbH – Briefpapier</title>
<link rel="stylesheet" href="https://fonts.googleapis.com/css2?family=Source+Sans+3:wght@300;400&display=swap">
<style>
  :root {
    --navy: #232a3d;
    --silver: #c9ccd3;
    --paper: #fbfbfb;
    --backdrop: #e9eaeb;
    --text-grey: #6d7079;
    --rule-grey: #9a9ca1;
    --band-grey: #a7a9ad;
  }
  * { box-sizing: border-box; margin: 0; padding: 0; }
  html, body {
    width: 1200px; height: 954px; overflow: hidden;
    background: var(--backdrop);
    font-family: "Source Sans 3", "Source Sans Pro", Arial, sans-serif;
  }
  .letterhead {
    position: absolute; left: 282px; top: 27px;
    width: 636px; height: 900px;
    background: var(--paper);
    box-shadow: 0 2px 10px rgba(0,0,0,0.08);
    overflow: hidden;
  }
  .brand-block {
    position: absolute; left: 64px; top: 56px;
    width: 200px; height: 62px;
    background: var(--navy);
    display: flex; align-items: center; justify-content: center;
  }
  .brand-name {
    color: var(--silver);
    font-weight: 300; font-size: 27px;
    letter-spacing: 0.2em; text-transform: uppercase;
    padding-left: 0.2em;
  }
  .footer {
    position: absolute; left: 64px; right: 40px; bottom: 34px;
    display: flex; align-items: flex-end;
    color: var(--text-grey); font-size: 10px; line-height: 1.45;
  }
  .footer-col { padding-right: 14px; }
  .footer-col + .footer-col {
    border-left: 1px solid var(--rule-grey);
    padding-left: 12px;
  }
  .footer-address { margin-right: auto; border: 0; }
  .contact-list { list-style: none; }
  .contact-list li { display: flex; align-items: center; gap: 6px; }
  .contact-icon { width: 10px; height: 10px; flex: none; }
  .base-band {
    position: absolute; left: 0; right: 0; bottom: 0; height: 8px;
  }
  .base-band-navy {
    position: absolute; left: 0; bottom: 0; width: 66%; height: 5px;
    background: var(--navy);
    clip-path: polygon(0 0, 100% 0, calc(100% - 4px) 100%, 0 100%);
  }
  .base-band-grey {
    position: absolute; right: 0; bottom: 0; width: 34.6%; height: 5px;
    background: var(--band-grey);
    clip-path: polygon(4px 0, 100% 0, 100% 100%, 0 100%);
  }
</style>
</head>
<body>
  <main class="letterhead">
    <header class="brand-block">
      <span class="brand-name">Hollwen</span>
    </header>

    <footer class="footer">
      <div class="footer-col footer-address">
        Hollwen GmbH<br>
        Lindauer Weg 52, 80339 München
      </div>
      <div class="footer-col footer-contact">
        <ul class="contact-list">
          <li>
            <svg class="contact-icon" viewBox="0 0 10 10" aria-hidden="true"><circle cx="5" cy="5" r="5" fill="#232a3d"/><path d="M3.4 2.6l1 1-.5.6c.3.6.8 1.1 1.4 1.4l.6-.5 1 1-.6.8C4.8 6.8 3.2 5.2 2.8 3.7z" fill="#fff"/></svg>
            +49 (0)89 58210946
          </li>
          <li>
            <svg class="contact-icon" viewBox="0 0 10 10" aria-hidden="true"><circle cx="5" cy="5" r="5" fill="#232a3d"/><rect x="2.6" y="3.3" width="4.8" height="3.4" fill="none" stroke="#fff" stroke-width=".7"/><path d="M2.6 3.3L5 5.2l2.4-1.9" fill="none" stroke="#fff" stroke-width=".7"/></svg>
            info@hollwenbeta.example
          </li>
          <li>
            <svg class="contact-icon" viewBox="0 0 10 10" aria-hidden="true"><circle cx="5" cy="5" r="5" fill="#232a3d"/><circle cx="5" cy="5" r="2.5" fill="none" stroke="#fff" stroke-width=".6"/><path d="M2.5 5h5M5 2.5c-1.2 1.4-1.2 3.6 0 5M5 2.5c1.2 1.4 1.2 3.6 0 5" fill="none" stroke="#fff" stroke-width=".5"/></svg>
            www.hollwenbeta.example
          </li>
        </ul>
      </div>
      <div class="footer-col footer-legal">
        Dipl.-Wirtschaftsing. (FH) Till Osterwald<br>
        Munich district court HRB 527081<br>
        DE918204 5571 0009 1826 40
      </div>
    </footer>

    <div class="base-band" aria-hidden="true">
      <span class="base-band-navy"></span>
      <span class="base-band-grey"></span>
    </div>
  </main>
</body>
</html>
```